Redesign of Plastic Surgeon Website to fully responsive / modern feel

Hi

Our current website is out of date www.harbourlinecosmetic.org

We want a fresh / modern looking design
Needs to be fully responsive design that works extremely well on ipad and mobile device

Would like design for both full screen website and mobile

Have listed a few websites of other plastic surgeons we like
http://www.reformclinicplus.com/
http://www.doriankeelermd.com/
http://www.tarrantcontours.com/
http://www.oakdenecosmeticsurgery.com/

Menu needs to include
1. About Us
2. Procedures (see current website for example)
3. News
4. Patient Resources
5. Contact Us

We are flexible with colours / images / layout

I have uploaded a document that has some content - the face pages content is completed only

some of the procedures can have content upwards of 4000 words - total website can be large with over 40,000 words
Updates

Hi I have updated the logo for our design for the new website - this is the logo and colours we want reflected throughout the siteThanks Added Wednesday, January 13, 2016

Target Market(s)

Mainly women 20-60 85% of practice
Some men 15%

Industry/Entity Type

Plastic Surgery

Number of Pages Required

5+ page

Requirements
Must have
• We need designs for
• Homepage
• Internal pages
• 1. Landing pages for breast / body / face / non surgical main pages
• 2. Procedure pages for individual pages under each section - eg breast augmentation
• 3. About us pages - like meet the doctor, our staff, clinics
• 4. Contact page
• 5. Blog / News page
Nice to have
• See our list of websites for examples of designs we like
• Like full screen design with nice hero image
• Needs to have good to call to action messages on home page like
• Specials, procedure of the month, etc

```html
<!DOCTYPE html>
<html lang="en">
<head>
<meta charset="utf-8">
<title>Harbourline Cosmetic Institute – Surgical Procedures</title>
<link href="https://fonts.googleapis.com/css2?family=Roboto:wght@400;500;700&display=swap" rel="stylesheet">
<style>
:root{
  --magenta:#c53aa8;
  --magenta-light:#d84cba;
  --magenta-dark:#b22f97;
  --ink:#222;
  --muted:#888;
  --line:#e3e3e3;
  --hero:#4a4a4a;
  --footer:#464646;
  --footer-base:#3a3a3a;
  --footer-text:#bdbdbd;
  --white:#fff;
}
*{box-sizing:border-box;margin:0;padding:0}
html,body{width:672px;height:1200px;overflow:hidden}
body{position:relative;background:var(--white);font-family:'Roboto',Arial,sans-serif;color:var(--ink)}
ul{list-style:none}

.top-bar{position:absolute;left:0;top:0;width:672px;height:24px;border-bottom:1px solid var(--line);font-size:7px;font-weight:500}
.top-bar .info{position:absolute;left:138px;top:8px;letter-spacing:.3px}
.top-bar .social{position:absolute;right:78px;top:8px;display:flex;gap:11px}
.dot{width:6px;height:6px;border-radius:50%;background:#333}
.top-bar .search{position:absolute;right:82px;top:6px}
.top-bar .search{right:76px}

.brand{position:absolute;left:33px;top:0;width:88px;height:100px}
.brand svg{position:absolute;left:0;top:0}
.brand-name{position:absolute;left:6px;top:14px;width:76px;text-align:center;color:var(--white);font-size:9px;font-weight:500;line-height:1.35;letter-spacing:.6px;text-transform:uppercase}

.main-nav{position:absolute;left:137px;top:32px;display:flex;font-size:7px;font-weight:700;text-transform:uppercase;letter-spacing:.2px}
.main-nav li{text-align:center;line-height:1.45}
.main-nav li:nth-child(1){width:57px}
.main-nav li:nth-child(2){width:66px;margin-left:5px}
.main-nav li:nth-child(3){width:52px;margin-left:4px}
.main-nav li:nth-child(4){width:86px;margin-left:8px}
.main-nav li:nth-child(5){width:66px;margin-left:6px}
.main-nav li:nth-child(6){width:64px;margin-left:6px}
.main-nav li:nth-child(7){width:24px;margin-left:10px}
.main-nav li:nth-child(8){width:40px;margin-left:12px}

.hero{position:absolute;left:0;top:57px;width:672px;height:158px;background:radial-gradient(ellipse at 50% 30%,#6a6a6a 0%,#4b4b4b 45%,#3c3c3c 100%)}
.hero h1{position:absolute;left:0;right:0;top:52px;text-align:center;color:var(--white);font-size:28px;font-weight:500;letter-spacing:.5px}
.breadcrumb{position:absolute;left:0;right:0;top:87px;text-align:center;color:var(--white);font-size:6.5px;font-weight:500}
.breadcrumb span{margin:0 6px}

.tab-label{position:absolute;left:240px;top:240px;width:191px;height:19px;background:#111;color:var(--white);font-size:7.5px;letter-spacing:1px;text-align:center;line-height:19px;text-transform:uppercase}
.tab-label em{font-style:normal;color:var(--magenta-light)}

.procedure-card{position:absolute;left:86px;width:501px;height:166px;border:1px solid var(--line);background:var(--white)}
.procedure-card.c1{top:307px}.procedure-card.c2{top:494px}.procedure-card.c3{top:680px}
.procedure-card h2{position:absolute;left:21px;top:27px;font-size:7.5px;font-weight:500;text-transform:uppercase}
.procedure-card .duration{position:absolute;left:21px;top:41px;font-size:7.5px;color:var(--muted)}
.price{position:absolute;left:22px;top:66px;width:68px;height:19px;background:var(--magenta);color:var(--white);font-size:10px;text-align:center;line-height:19px}
.procedure-photo{position:absolute;left:180px;top:-1px;width:140px;height:166px}
.c1 .procedure-photo{background:linear-gradient(160deg,#3a1d12 0%,#a9482a 45%,#d9a78d 60%,#2c1a14 100%)}
.c2 .procedure-photo{background:linear-gradient(150deg,#ededed 0%,#8a6a5a 35%,#5b3a2c 60%,#efe9e6 100%)}
.c3 .procedure-photo{background:linear-gradient(160deg,#2a2a2a 0%,#6a4a44 35%,#b21e2a 65%,#f4f4f4 100%)}
.procedure-body{position:absolute;left:346px;top:32px;width:140px;font-size:6.5px;color:var(--muted);line-height:1.55}
.procedure-links{margin-top:8px}
.procedure-links li{font-size:7.2px;color:var(--ink);line-height:12.4px;padding-left:15px;position:relative}
.procedure-links li::before{content:"»";position:absolute;left:3px;font-weight:700}

.site-footer{position:absolute;left:0;top:939px;width:672px;height:218px;background:var(--footer)}
.contact-strip{position:absolute;left:33px;top:908px;width:605px;height:62px;display:flex;z-index:2;color:var(--white)}
.contact-item{position:relative;height:62px;background:var(--magenta)}
.contact-item:nth-child(1){width:191px}
.contact-item:nth-child(2){width:207px;background:var(--magenta-light)}
.contact-item:nth-child(3){width:207px;background:var(--magenta-dark)}
.contact-item svg{position:absolute;left:20px;top:23px}
.contact-item h3{position:absolute;left:46px;top:17px;font-size:7.5px;font-weight:700;text-transform:uppercase}
.contact-item p{position:absolute;left:46px;top:30px;font-size:6.5px;line-height:1.4;color:#f6dff1}
.contact-item:nth-child(2) svg{left:25px}
.contact-item:nth-child(2) h3,.contact-item:nth-child(2) p{left:55px}
.contact-item:nth-child(3) svg{left:25px}
.contact-item:nth-child(3) h3,.contact-item:nth-child(3) p{left:55px}

.footer-brand{position:absolute;left:86px;top:70px;width:70px;color:var(--footer-text);font-size:11px;line-height:1.55;text-align:center;text-transform:uppercase;letter-spacing:.6px}
.footer-heading{position:absolute;top:59px;color:var(--white);font-size:10px;font-weight:500}
.footer-heading::after{content:"";position:absolute;left:0;top:16px;width:32px;height:2px;background:var(--magenta)}
.services-heading{left:249px}.news-heading{left:466px}
.service-list{position:absolute;top:93px;font-size:6.5px;color:var(--footer-text)}
.service-list li{line-height:16.4px}
.service-list li::before{content:"› ";}
.service-list.a{left:249px}.service-list.b{left:323px}
.newsletter-text{position:absolute;left:466px;top:94px;width:170px;font-size:6.5px;line-height:1.5;color:var(--footer-text)}
.newsletter-form{position:absolute;left:466px;top:122px;width:172px;height:18px;display:flex}
.newsletter-form .field{flex:1;background:#333;color:var(--footer-text);font-size:6.5px;padding-left:6px;line-height:18px}
.newsletter-form .send{width:52px;background:var(--magenta);color:var(--white);font-size:6.5px;font-weight:700;text-align:center;line-height:18px}
.stay{position:absolute;left:466px;top:152px;font-size:6.5px;font-weight:500;color:var(--white);text-transform:uppercase}
.footer-social{position:absolute;left:468px;top:174px;display:flex;gap:17px}
.footer-social .dot{background:var(--footer-text)}
.footer-base{position:absolute;left:0;top:1157px;width:672px;height:43px;background:var(--footer-base);color:var(--footer-text);text-align:center;font-size:6.3px}
.footer-base .copy{margin-top:9px}
.footer-base .links{margin-top:7px;letter-spacing:1.2px}
</style>
</head>
<body>

<header>
  <div class="top-bar">
    <div class="info">INFO &amp; RESERVATIONS : &nbsp;02 5550 1842</div>
    <div class="social" style="right:96px"><span class="dot"></span><span class="dot"></span><span class="dot"></span><span class="dot"></span></div>
    <svg class="search" width="9" height="9" viewBox="0 0 10 10"><circle cx="4" cy="4" r="3" fill="none" stroke="#333" stroke-width="1.4"/><line x1="6.2" y1="6.2" x2="9.3" y2="9.3" stroke="#333" stroke-width="1.5"/></svg>
  </div>

  <div class="brand">
    <svg width="88" height="100" viewBox="0 0 88 100"><polygon points="0,0 88,0 88,68 0,100" fill="var(--magenta)"/></svg>
    <div class="brand-name">Harbourline Cosmetic Institute</div>
  </div>

  <ul class="main-nav">
    <li>Our Practice</li>
    <li>Surgical<br>Proc edures</li>
    <li>News &amp; Views</li>
    <li>Before After Photos</li>
    <li>Plastic<br>Surgery Reviews</li>
    <li>Patient<br>Preparation</li>
    <li>FAQ</li>
    <li>Contact</li>
  </ul>
</header>

<section class="hero" role="img" aria-label="Close-up portrait photograph of a woman in greyscale">
  <h1>SURGICAL PROC EDURES</h1>
  <div class="breadcrumb">HOME<span>»</span>SURGICAL PROC EDURES</div>
</section>

<main>
  <div class="tab-label"><em>Foreheadplasty</em> – Brow Lift</div>

  <article class="procedure-card c1">
    <h2>Brow Lift Plastic Surgery Sydney</h2>
    <p class="duration">Time Duration : 25 - 35 min</p>
    <div class="price">$47.00</div>
    <div class="procedure-photo" role="img" aria-label="Photo of a smiling woman with long curly red hair"></div>
    <div class="procedure-body">
      <p>The secret to the motion and the breathtaking volume of this long hair look is purely in the styling.</p>
      <ul class="procedure-links">
        <li>What is Foreheadplasty Brow Lift?</li><li>The Problem</li><li>Your Pre-operative Brow Lift Visit</li><li>Realistic Expectations</li><li>Ancillary Procedures</li><li>Your Surgical Experience</li>
      </ul>
    </div>
  </article>

  <article class="procedure-card c2">
    <h2>Brow Lift Plastic Surgery Sydney</h2>
    <p class="duration">Time Duration : 25 - 35 min</p>
    <div class="price">$47.00</div>
    <div class="procedure-photo" role="img" aria-label="Photo of a woman with long brown wavy hair"></div>
    <div class="procedure-body">
      <p>The secret to the motion and the breathtaking volume of this long hair look is purely in the styling.</p>
      <ul class="procedure-links">
        <li>What is Foreheadplasty Brow Lift?</li><li>The Problem</li><li>Your Pre-operative Brow Lift Visit</li><li>Realistic Expectations</li><li>Ancillary Procedures</li><li>Your Surgical Experience</li>
      </ul>
    </div>
  </article>

  <article class="procedure-card c3">
    <h2>Brow Lift Plastic Surgery Sydney</h2>
    <p class="duration">Time Duration : 25 - 35 min</p>
    <div class="price">$47.00</div>
    <div class="procedure-photo" role="img" aria-label="Fashion photo of a woman in a red dress with dark feathers"></div>
    <div class="procedure-body">
      <p>The secret to the motion and the breathtaking volume of this long hair look is purely in the styling.</p>
      <ul class="procedure-links">
        <li>What is Foreheadplasty Brow Lift?</li><li>The Problem</li><li>Your Pre-operative Brow Lift Visit</li><li>Realistic Expectations</li><li>Ancillary Procedures</li><li>Your Surgical Experience</li>
      </ul>
    </div>
  </article>
</main>

<div class="contact-strip">
  <div class="contact-item">
    <svg width="11" height="15" viewBox="0 0 11 15"><path d="M5.5 0C2.5 0 0 2.4 0 5.4 0 9.3 5.5 15 5.5 15S11 9.3 11 5.4C11 2.4 8.5 0 5.5 0z" fill="#fff"/><circle cx="5.5" cy="5.4" r="2" fill="var(--magenta)"/></svg>
    <h3>Hospital Address</h3>
    <p>E12, Quay Lane, Harbour Corner<br>Sydney - 008</p>
  </div>
  <div class="contact-item">
    <svg width="14" height="14" viewBox="0 0 14 14"><path d="M3 0.5l2.2 3-1.3 1.8c.9 1.9 2.3 3.3 4.2 4.2l1.8-1.3 3 2.2-1.2 2.6C7 13 1 7 .4 1.7z" fill="#fff"/></svg>
    <h3>Emergency ( 24X7 )</h3>
    <p>02 5550 1842<br>Call Us Now- 24/7 Customer Suppor</p>
  </div>
  <div class="contact-item">
    <svg width="15" height="11" viewBox="0 0 15 11"><rect x=".75" y=".75" width="13.5" height="9.5" rx="1" fill="none" stroke="#fff" stroke-width="1.5"/><path d="M1 1.2l6.5 5 6.5-5" fill="none" stroke="#fff" stroke-width="1.5"/></svg>
    <h3>Hospital Address</h3>
    <p>info@harbourlineclinic.com<br>care@harbourlineclinic.com</p>
  </div>
</div>

<footer class="site-footer">
  <div class="footer-brand">Harbourline Cosmetic Institute</div>

  <h4 class="footer-heading services-heading">OUR SERVICES</h4>
  <ul class="service-list a"><li>Births</li><li>Pulmonary</li><li>Cardiology</li><li>Neurology</li><li>Traumatology</li><li>Neurology</li></ul>
  <ul class="service-list b"><li>Dental</li><li>Nuclear magnetic</li><li>Pregnancy</li><li>For disabled</li><li>X-ray</li><li>Prosthese</li></ul>

  <h4 class="footer-heading news-heading">NEWSLETTER</h4>
  <p class="newsletter-text">Accusamus et iusto odio dignissimos ducimus blanditiis praesentium quas molestias excep.</p>
  <div class="newsletter-form"><span class="field">Email Address</span><span class="send">SEND</span></div>
  <p class="stay">Stay Connected</p>
  <div class="footer-social"><span class="dot"></span><span class="dot"></span><span class="dot"></span><span class="dot"></span></div>
</footer>

<div class="footer-base">
  <p class="copy">© Harbourline Cosmetic Institute Dr Elliot Marsh Cosmetic Surgery Sydney Australia</p>
  <p class="links">Home | Disclaimer | Privacy | Sitemap | Feedback | Tell a friend | Contact Us | Find us on Maps</p>
</div>

</body>
</html>
```